A simple Chatterbook Ad (not Chatterbook Page) for weight loss surgery

It’s a simple ad in terms of the text.

The text should say:
Curious about weight loss surgery?
This 30 second quiz will tell you which procedure will suit you best

I'm open to variations in the text if it is thought to enhance the ad.

Targeted towards obese individuals who have been unable to lose weight with diet and exercise. My industry is weight loss surgery – webpage www.marcusbellweather.com.au. Clicking the ad leads to a quiz on my webpage relating to weight loss surgery. Most frequent users of this service are females (75%) between ages of 35 and 55 years.

Successful weight loss surgery can enable individuals who have been unable to lose weight to lose a substantial amount of the excess weight they are carrying to be healthier and happier.

```html
<!DOCTYPE html>
<html lang="en">
<head>
<meta charset="UTF-8">
<title>Weight Loss Surgery Quiz Ad</title>
<link href="https://fonts.googleapis.com/css2?family=Poppins:wght@400;600;700&display=swap" rel="stylesheet">
<style>
  :root {
    --navy: #1f2466;
    --navy-deep: #1a1f5c;
    --orange: #ff5500;
    --white: #ffffff;
    --photo-tone: #5a4660;
  }
  html, body {
    margin: 0;
    padding: 0;
    width: 1200px;
    height: 1200px;
    overflow: hidden;
    background: var(--navy);
  }
  .ad {
    position: relative;
    width: 1200px;
    height: 1200px;
    overflow: hidden;
    background: radial-gradient(circle at 75% 40%, #232a75 0%, var(--navy) 55%, var(--navy-deep) 100%);
    font-family: "Poppins", sans-serif;
    color: var(--white);
  }
  .hero-photo {
    position: absolute;
    left: 0;
    top: 0;
    width: 640px;
    height: 1200px;
    background: linear-gradient(90deg, var(--photo-tone) 0%, var(--photo-tone) 45%, rgba(31,36,102,0) 100%);
  }
  .hashtag {
    position: absolute;
    left: 567px;
    top: 234px;
    margin: 0;
    font-weight: 700;
    font-size: 22px;
    line-height: 22px;
    color: var(--orange);
  }
  .headline {
    position: absolute;
    left: 567px;
    top: 308px;
    margin: 0;
    font-weight: 700;
    font-size: 75px;
    line-height: 106px;
    text-transform: uppercase;
    letter-spacing: -1px;
    white-space: nowrap;
    text-shadow: 0 4px 18px rgba(0,0,0,0.3);
  }
  .subline {
    position: absolute;
    left: 567px;
    top: 806px;
    margin: 0;
    font-weight: 400;
    font-size: 26px;
    line-height: 53px;
    letter-spacing: 4px;
    white-space: nowrap;
  }
  .cta {
    position: absolute;
    left: 567px;
    top: 1056px;
    width: 397px;
    height: 81px;
    box-sizing: border-box;
    border: 4px solid var(--white);
    border-radius: 41px;
    background: var(--orange);
    color: var(--white);
    font-weight: 600;
    font-size: 27px;
    display: flex;
    align-items: center;
    justify-content: center;
    text-decoration: none;
    box-shadow: 0 6px 20px rgba(0,0,0,0.35);
  }
</style>
</head>
<body>
  <div class="ad">
    <div class="hero-photo" role="img" aria-label="Photo of a woman in dark underwear measuring her waist with a yellow tape measure"></div>
    <p class="hashtag">#mybodygoals</p>
    <h1 class="headline">Curious<br>about<br>weight loss<br>surgery?</h1>
    <p class="subline">This 30 second quiz will tell<br>you which procedure will<br>suit you best.</p>
    <a class="cta" href="#">Start now</a>
  </div>
</body>
</html>
```